Mixed Martial Arts Business Book Cover

Dorian Kessel Jr aka The Dojo Profit Mentor Presents

The name of my book is

"My Studio Fortune Roadmap"

tagline is

"The Gloves Off Manual For Growing Your Fight Gym Into A TRUE Enterprise"

I would like like my image incorporated some how

Target Market(s)

mixed martial arts and brazilian jiu jitsu school owners

Industry/Entity Type

Business

Requirements
Must have
• The image I provided incorporated some how (unless) yiou just think its stupid and wont work
Nice to have
• these guys own schools teach people in the GXL cage fighting so I'm not sure but the gxl cage fence ( a fence look) may be cool, or maybe not but i'm not opposedto seeing a design with a cage/fence also
• nice to have the image i provided if possible
Should not have
• should not have any images of random fighters

```html
<!DOCTYPE html>
<html lang="en">
<head>
<meta charset="utf-8">
<title>My Studio Fortune Roadmap — Book Cover</title>
<link href="https://fonts.googleapis.com/css2?family=Anton&family=Barlow+Condensed:ital,wght@1,700&family=Fjalla+One&family=Russo+One&family=Saira+Condensed:wght@700&display=swap" rel="stylesheet">
<style>
  :root {
    --ink-white: #ffffff;
    --brand-red: #c4161c;
    --bg-center: #3a3a3a;
    --bg-mid: #1e1e1e;
    --bg-edge: #080808;
  }
  html, body {
    margin: 0;
    padding: 0;
    overflow: hidden;
    background: var(--bg-edge);
  }
  .cover {
    position: relative;
    width: 800px;
    height: 1200px;
    overflow: hidden;
    color: var(--ink-white);
  }
  .cover-backdrop {
    position: absolute;
    inset: 0;
    background: radial-gradient(ellipse 70% 55% at 50% 42%, var(--bg-center) 0%, var(--bg-mid) 55%, var(--bg-edge) 100%);
  }
  .line {
    position: absolute;
    left: 0;
    width: 800px;
    margin: 0;
    text-align: center;
    line-height: 1;
    white-space: nowrap;
    text-shadow: 0 4px 8px rgba(0,0,0,0.6);
  }
  .book-title { margin: 0; }
  .author-name {
    top: 24px;
    font-family: "Saira Condensed", sans-serif;
    font-weight: 700;
    font-style: italic;
    font-size: 44px;
    letter-spacing: 7px;
  }
  .author-title {
    top: 74px;
    font-family: "Fjalla One", sans-serif;
    font-size: 42px;
    letter-spacing: -0.5px;
  }
  .accent { color: var(--brand-red); }
  .title-lead {
    top: 232px;
    font-family: "Anton", sans-serif;
    font-size: 140px;
  }
  .title-main {
    top: 438px;
    font-family: "Russo One", sans-serif;
    font-size: 158px;
    color: var(--brand-red);
    letter-spacing: -4px;
  }
  .title-sub {
    top: 640px;
    font-family: "Fjalla One", sans-serif;
    font-size: 148px;
    letter-spacing: 1px;
  }
  .tagline {
    font-family: "Barlow Condensed", sans-serif;
    font-weight: 700;
    font-style: italic;
    font-size: 44px;
    letter-spacing: -0.5px;
  }
  .tagline-one { top: 1058px; }
  .tagline-two { top: 1114px; }
</style>
</head>
<body>
  <main class="cover">
    <div class="cover-backdrop" role="img" aria-label="Dark grunge background with a cage fence texture"></div>

    <p class="line author-name">Dorian Kessel Jr</p>
    <p class="line author-title">AKA The <span class="accent">Dojo</span> Profit Mentor Presents</p>

    <h1 class="book-title">
      <span class="line title-lead">MY STUDIO</span>
      <span class="line title-main">FORTUNE</span>
      <span class="line title-sub">ROADMAP</span>
    </h1>

    <p class="line tagline tagline-one">The Gloves Off Manual For</p>
    <p class="line tagline tagline-two">Growing Your Fight Gym Into <span class="accent">A TRUE Enterprise</span></p>
  </main>
</body>
</html>
```